Business Card Design for a Private Label Pet Company

We need a business card design for our family-owned company, Hollow Creek Pet Works (www.hollowcreekpetworks.com), out of St. Louis, MO. We provide turnkey private label solutions for retailers, Marketvale sellers and other brands who want to provide high quality, natural, Made in the USA pet products to their customers. Our customer are worldwide and range from the US to the UK to Vietnam and beyond. We offer private label for dozens of pet products including grooming products (shampoos, conditioners, colognes, ear and eye washes, mouthwash, etc.), all meat treats, supplements, and specialty products (pet stain and odor cleaner, anti-chew spray, etc.). We would like to see designs that use the colors, fonts and logos (see variations) within our brand guidelines and fit with the look and feel from our website.

Target Market(s)

Pet Store Owners, Marketvale Sellers, Pet Brand Marketers

Industry/Entity Type

Pet

Contact Information for Business Card

Tom Willoughby
CEO
Hollow Creek Pet Works
5817 Brookhaven Commerce Lane
St. Louis, MO 63521
office: 314.555.0182
mobile: 770.555.0139
email: tom@hollowcreekpetworks.com

Colors

Designer to choose colors to be used in the design.

Requirements
Must have
• Need to follow the brand guidelines attached for colors, fonts and logos
• Need to use the logos attached (or a variation) with our without the tagline
• Name, title, phone (office and mobil), email, address on the business card
• Clean professional look and feel that says: high quality natural pet products, high quality service, made in the USA
Nice to have
• Made in the USA is a big positive in our industry and we are very proud of it. There is an attached icon from our website. The designer can get creative here as they wish.
• I do like using color for pop. Just don't like lots of bright, loud colors.
Should not have
• lots of bright, loud colors
• overwhelming to the reader
• crowded

```html
<!DOCTYPE html>
<html lang="en">
<head>
<meta charset="utf-8">
<title>Hollow Creek Pet Works — Business Card</title>
<link href="https://fonts.googleapis.com/css2?family=Montserrat:wght@400;500;800&family=Raleway:wght@500&display=swap" rel="stylesheet">
<style>
  :root {
    --olive: #6b8a3e;
    --slate: #41595a;
    --paper: #ffffff;
    --ink: #1d1f20;
    --rule: #c9c9c0;
    --seal-ring: #b8ad8a;
    --seal-core: #d9d3bf;
    --backdrop: #e9eae6;
  }
  * { box-sizing: border-box; margin: 0; padding: 0; }
  html, body { width: 1200px; height: 782px; overflow: hidden; background: var(--backdrop); }
  .canvas {
    width: 1200px; height: 782px;
    display: flex; align-items: center; justify-content: center; gap: 40px;
    font-family: "Montserrat", sans-serif;
  }
  .card {
    position: relative; width: 540px; height: 309px; overflow: hidden;
    box-shadow: 0 6px 18px rgba(0,0,0,.18);
  }
  .card svg.shapes { position: absolute; inset: 0; }

  /* Front */
  .card--front { background: var(--olive); }
  .front__brand {
    position: absolute; left: 190px; top: 58px; width: 330px;
    color: var(--paper); font-weight: 800; font-size: 30px; line-height: 1.05;
    letter-spacing: .5px; text-transform: uppercase; text-align: center;
    white-space: nowrap;
  }
  .front__tagline {
    position: absolute; left: 210px; top: 200px; width: 320px;
    font-family: "Raleway", sans-serif; font-weight: 500;
    font-size: 17px; letter-spacing: 1px; color: var(--slate);
    text-transform: uppercase; white-space: nowrap;
  }

  /* Back */
  .card--back { background: var(--paper); }
  .back__name {
    position: absolute; left: 62px; top: 22px;
    font-weight: 800; font-size: 17px; color: var(--slate); text-transform: uppercase;
    white-space: nowrap;
  }
  .back__title { position: absolute; left: 62px; top: 43px; font-size: 11px; color: var(--slate); }
  .back__contacts {
    position: absolute; left: 34px; top: 118px; list-style: none;
    font-size: 12.5px; color: var(--ink); line-height: 19px;
  }
  .back__contacts li { display: flex; align-items: center; gap: 6px; white-space: nowrap; }
  .back__contacts svg { width: 11px; height: 11px; fill: var(--slate); flex: none; }
  .back__brand {
    position: absolute; left: 282px; top: 100px; width: 246px;
    font-weight: 800; font-size: 24px; line-height: 1.1; color: var(--slate);
    text-transform: uppercase; text-align: center; white-space: nowrap;
  }
  .back__rule { position: absolute; left: 300px; top: 166px; width: 210px; height: 1px; background: var(--rule); }
  .back__address {
    position: absolute; right: 26px; top: 205px; text-align: left;
    font-size: 14px; line-height: 18px; color: var(--ink); white-space: nowrap;
  }
</style>
</head>
<body>
<main class="canvas">

  <section class="card card--front" aria-label="Business card front">
    <svg class="shapes" viewBox="0 0 540 309" aria-hidden="true">
      <polygon points="0,100 120,100 120,180 540,180 540,240 0,240" fill="var(--paper)"/>
      <circle cx="95" cy="148" r="72" fill="var(--olive)"/>
      <circle cx="95" cy="148" r="62" fill="var(--seal-ring)"/>
      <circle cx="95" cy="148" r="46" fill="var(--seal-core)"/>
    </svg>
    <div class="front__brand">Hollow Creek<br>Pet Works</div>
    <p class="front__tagline">Turnkey Private Label Partner</p>
  </section>

  <section class="card card--back" aria-label="Business card back">
    <svg class="shapes" viewBox="0 0 540 309" aria-hidden="true">
      <polygon points="0,0 45,0 18,32 0,32" fill="var(--slate)"/>
      <polygon points="45,0 55,0 55,32 18,32" fill="var(--olive)"/>
      <polygon points="0,262 290,262 268,309 0,309" fill="var(--slate)"/>
      <polygon points="290,262 540,262 540,309 268,309" fill="var(--olive)"/>
    </svg>
    <h1 class="back__name">Tom Willoughby</h1>
    <p class="back__title">CEO</p>
    <ul class="back__contacts">
      <li><svg viewBox="0 0 12 12"><path d="M2 1h3l1 3-2 1a7 7 0 0 0 3 3l1-2 3 1v3c0 1-1 1-1 1A10 10 0 0 1 1 2s0-1 1-1z"/></svg>314.555.0182</li>
      <li><svg viewBox="0 0 12 12"><path d="M3 0h6v12H3zM4 1v9h4V1z"/></svg>770.555.0139</li>
      <li><svg viewBox="0 0 12 12"><path d="M0 2h12v8H0zM1 3l5 4 5-4z"/></svg>tom@hollowcreekpetworks.com</li>
      <li><svg viewBox="0 0 12 12"><circle cx="6" cy="6" r="6"/></svg>www.hollowcreekpetworks.com</li>
    </ul>
    <div class="back__brand">Hollow Creek<br>Pet Works</div>
    <div class="back__rule"></div>
    <p class="back__address">5817 Brookhaven Commerce<br>Lane St. Louis, MO 63521</p>
  </section>

</main>
</body>
</html>
```